Business Card Design

General Brief:
Varnel Works is a newly established international manufacturing company. We have a manufacturing facility in China and are in the process of building a new facility in Brazil and are expanding into Africa, the Middle East and Western markets by marketing our products through a licensee program. We use production line manufacture processes (similar to the automotive industry) to produce houses, apartments, hotels and accommodation for the resource sector. We will need to be able to differentiate between the various regions that we serve and the market we operate in.

Key Words to describe our business:
International, Global, Professional, Quality, Standard Compliant, Designful, Cost Effective, Experienced

General Brief:
We need business card designs which cater for the possibility of differentiating the various regions that we serve and the market we operate in. Also, we need a secondary typography selection which suits the primary typography used in the corporate signature (please always state which font is being applied so as to cross-check for the necessary font licenses). First print will be made for our Chinese head office and division, therefore will have the special prerequisite of featuring two distinct languages: English-speaking and Chinese. We assume that a double sided version (recto/verso) could work best in order to separate the languages—other creative interpretations, options and integrations are welcome.

Logo Symbolism:
A dot might seem to be an unassuming little thing, the first mark on the pristine sheet of paper. In this case, the dot is a beginning. But see what just happened there? The dot, an essential component in the structure of the sentence, closed it, making it a symbol of ending. Therefore, the dot is both an origination and a conclusion, encompassing all the possibilities of the universe within it, a seed full of potential and a symbol of the supreme being. The dot is also called the "bindhu," which means "drop." The bindhu is a symbol of the absolute, marked on the forehead at the position of the third eye in the place believed to be the seat of the soul. The presence of dots outside or within a symbol can signify the presence of something else. It also acts as reminder of the concept of space and all in all performs as a very positive symbol in the Varnel Works logo.

Target Market(s)

See Stationary Project

Industry/Entity Type

Accommodation

Requirements
Must have
• See Stationary Project

Logo on Stationary Project

```html
<!DOCTYPE html>
<html lang="en">
<head>
<meta charset="utf-8">
<title>Varnel Works – Business Card Design</title>
<link rel="stylesheet" href="https://fonts.googleapis.com/css2?family=Open+Sans:wght@400;600;700&display=swap">
<style>
  :root {
    --stage-light: #e6e6e9;
    --stage-dark: #231f20;
    --card-white: #ffffff;
    --brand-blue: #00adee;
    --brand-navy: #0b2a3f;
    --text-grey: #444448;
    --label-grey: #3a3a3c;
  }
  * { margin: 0; padding: 0; box-sizing: border-box; }
  html, body { width: 1200px; height: 800px; overflow: hidden; }
  body {
    position: relative;
    font-family: "Open Sans", Arial, sans-serif;
    background: linear-gradient(to bottom, var(--stage-light) 0 600px, var(--stage-dark) 600px 800px);
  }

  .side-label { position: absolute; color: var(--label-grey); font-size: 14px; line-height: 19px; }
  .side-label strong { font-size: 16px; font-weight: 700; margin-right: 7px; }
  .side-label--chinese { left: 144px; top: 38px; }
  .side-label--chinese strong { color: var(--brand-blue); }
  .side-label--chinese .note { display: block; font-weight: 700; font-size: 14px; }
  .side-label--english { right: 142px; top: 69px; }
  .side-label--english strong { color: #1d1d1f; }

  .card {
    position: absolute;
    width: 420px; height: 240px;
    background: var(--card-white);
    box-shadow: 0 1px 6px rgba(0,0,0,0.45);
    overflow: hidden;
  }
  .card--chinese { left: 140px; border-top-right-radius: 40px; }
  .card--english { left: 640px; border-top-left-radius: 40px; }
  .card--top { top: 130px; }
  .card--bottom { top: 430px; }
  .card--bottom::after {
    content: ""; position: absolute; left: 0; right: 0; top: 86px; bottom: 0;
    background: var(--brand-blue);
  }

  .dot { position: absolute; border-radius: 50%; background: var(--brand-blue); z-index: 1; }
  .dot--large { width: 56px; height: 56px; top: 11px; }
  .dot--medium { width: 18px; height: 18px; top: 52px; }
  .dot--small { width: 10px; height: 10px; top: 15px; }
  .card--chinese .dot--large { left: 353px; }
  .card--chinese .dot--medium { left: 311px; }
  .card--chinese .dot--small { left: 273px; }
  .card--english .dot--large { left: 11px; }
  .card--english .dot--medium { left: 91px; }
  .card--english .dot--small { left: 137px; }

  .wordmark {
    position: absolute; top: 32px; z-index: 1;
    color: var(--brand-navy); font-weight: 700; font-size: 20px; line-height: 28px;
  }
  .card--chinese .wordmark { left: 36px; }
  .card--english .wordmark { right: 36px; }

  .contact {
    position: absolute; top: 103px; z-index: 1;
    width: 280px;
    list-style: none; text-align: right;
    font-size: 9px; font-weight: 600; line-height: 13.2px;
    color: var(--text-grey); text-transform: uppercase;
  }
  .card--english .contact { right: 39px; }
  .card--chinese .contact { left: 28px; transform: scaleX(-1); }
  .card--bottom .contact { color: var(--card-white); }

  .pager { position: absolute; bottom: 26px; display: flex; gap: 8px; z-index: 1; }
  .pager span { width: 9px; height: 9px; border-radius: 50%; background: var(--brand-blue); }
  .card--bottom .pager span { background: var(--card-white); }
  .card--chinese .pager { right: 26px; }
  .card--english .pager { left: 25px; }
</style>
</head>
<body>

<p class="side-label side-label--chinese"><strong>CHINESE</strong>text will go this side<span class="note">Now used is only placeholder text</span></p>
<p class="side-label side-label--english"><strong>ENGLISH</strong>text will go this side</p>

<section class="card card--chinese card--top">
  <span class="dot dot--small"></span><span class="dot dot--medium"></span><span class="dot dot--large"></span>
  <div class="wordmark">Varnel Works</div>
  <ul class="contact">
    <li>International manufacturer of modular homes</li>
    <li>lorem@varnelworks.com</li>
    <li>Mobile: 0412738590</li>
    <li>Office: 0518834716</li>
    <li>14 Linden Street</li>
    <li>Heqiao Town</li>
    <li>Qinghe District Harbin City. China</li>
  </ul>
  <div class="pager"><span></span><span></span><span></span></div>
</section>

<section class="card card--english card--top">
  <span class="dot dot--large"></span><span class="dot dot--medium"></span><span class="dot dot--small"></span>
  <div class="wordmark">Varnel Works</div>
  <ul class="contact">
    <li>International manufacturer of modular homes</li>
    <li>lorem@varnelworks.com</li>
    <li>Mobile: 0412738590</li>
    <li>Office: 0518834716</li>
    <li>14 Linden Street</li>
    <li>Heqiao Town</li>
    <li>Qinghe District Harbin City. China</li>
  </ul>
  <div class="pager"><span></span><span></span><span></span></div>
</section>

<section class="card card--chinese card--bottom">
  <span class="dot dot--small"></span><span class="dot dot--medium"></span><span class="dot dot--large"></span>
  <div class="wordmark">Varnel Works</div>
  <ul class="contact">
    <li>International manufacturer of modular homes</li>
    <li>lorem@varnelworks.com</li>
    <li>Mobile: 0412738590</li>
    <li>Office: 0518834716</li>
    <li>14 Linden Street</li>
    <li>Heqiao Town</li>
    <li>Qinghe District Harbin City. China</li>
  </ul>
  <div class="pager"><span></span><span></span><span></span></div>
</section>

<section class="card card--english card--bottom">
  <span class="dot dot--large"></span><span class="dot dot--medium"></span><span class="dot dot--small"></span>
  <div class="wordmark">Varnel Works</div>
  <ul class="contact">
    <li>International manufacturer of modular homes</li>
    <li>lorem@varnelworks.com</li>
    <li>Mobile: 0412738590</li>
    <li>Office: 0518834716</li>
    <li>14 Linden Street</li>
    <li>Heqiao Town</li>
    <li>Qinghe District Harbin City. China</li>
  </ul>
  <div class="pager"><span></span><span></span><span></span></div>
</section>

</body>
</html>
```